Web design for Crowdfunding site HaloFundry.com

We need a web design for christian crowdfunding website. Here is the challenge: We need responsive layout that is targeted first in iPad size of screen. It should also scale somehow down to iPhone size of screens. Web layout can be about the same size as iPad screen.

Screens should work so that main page scrolls not but only certain part of the screen scrolls and always one "page" at time. We can implement these "scrolls" then later with javascript but now we need only design. The challenge is to create this kind of hybrid website / app look.

Target is at first to raise funds to orphan people needing about $40 per month for their living and education. There is always some organization which takes care of these kids. Later there will be other christian missions included. At first we are looking to find monthly supporters.

You can be as creative as you want :) As you see from the look and feel sector, I am not looking any same traditional look which many "help kids" sites have. I am looking to reach now younger generation and therefore iPad and mobile are the main screen sizes.

Inspirational designs:
- https://brightpixelhub.example/profiles/studiokelvira/designs/418263?from=%2Fbrowse%2Fxhr%2Fdesigns%3Fcategory%3Dmobile-app-design
- http://www.artmarketloop.example/design/7261540 Clear, simple visuals
- http://www.artmarketloop.example/design/8420917 Header
- http://www.artmarketloop.example/design/6394275 Contrast in the colors, i think is powerfull

Some terms could be: Kids play, kids are learning (in the school). No static posture but living like kids are. I wonder also how we could also add little bit gaming style even though the question is of reali life of real people. Giving should be rewarding.

Target Market(s)

People who want help other people.

Industry/Entity Type

Christian

Number of Pages Required

4 page

Requirements
Must have
• Homepage. Mission page (In my wireframes it was one kid).
Nice to have
• Other pages and some idea how to scroll. 4 pages is no must. If you feel easy, please give first some draft and I give comments on that.

```html
<!DOCTYPE html>
<html lang="en">
<head>
<meta charset="utf-8">
<title>Halo Fundry – Christian crowd funding</title>
<link rel="stylesheet" href="https://fonts.googleapis.com/css2?family=Raleway:wght@700;800&family=Open+Sans:ital,wght@0,400;0,600;1,400&display=swap">
<style>
  :root {
    --bar: #1c1917;
    --gold: #fdb10f;
    --white: #ffffff;
    --field-light: #c9a87c;
    --field-mid: #a98055;
    --field-dark: #6b4a30;
    --field-haze: #d8c2b4;
    --ring: rgba(236, 228, 218, 0.9);
    --ring-fill: rgba(236, 228, 218, 0.2);
    --avatar: rgba(236, 228, 218, 0.82);
  }
  * { box-sizing: border-box; margin: 0; padding: 0; }
  html, body { width: 1200px; height: 900px; overflow: hidden; background: var(--bar); }
  .screen { position: relative; width: 1200px; height: 900px; overflow: hidden; font-family: "Open Sans", sans-serif; color: var(--white); }

  .topbar { position: absolute; top: 0; left: 0; width: 1200px; height: 86px; background: var(--bar); z-index: 3; }
  .menu-toggle { position: absolute; left: 37px; top: 20px; width: 46px; height: 46px; border: 2px solid var(--gold); border-radius: 50%; }
  .menu-toggle span { position: absolute; left: 15px; width: 13px; height: 2.5px; background: var(--gold); border-radius: 1px; }
  .menu-toggle span:nth-child(1) { top: 15px; }
  .menu-toggle span:nth-child(2) { top: 20px; }
  .menu-toggle span:nth-child(3) { top: 25px; }
  .nav-link { position: absolute; left: 118px; top: 31px; font-family: "Raleway", sans-serif; font-weight: 700; font-size: 19px; letter-spacing: 0.2px; color: var(--white); text-decoration: none; }
  .search-icon { position: absolute; left: 304px; top: 31px; }
  .brand { position: absolute; left: 0; right: 0; top: 24px; text-align: center; font-family: "Raleway", sans-serif; font-weight: 800; font-size: 32px; letter-spacing: 0.5px; color: var(--white); }
  .btn { position: absolute; top: 20px; height: 47px; border-radius: 4px; font-family: "Raleway", sans-serif; font-weight: 700; font-size: 19px; line-height: 45px; text-align: center; text-decoration: none; }
  .btn-login { left: 921px; width: 110px; border: 1px solid var(--white); color: var(--gold); }
  .btn-signup { left: 1055px; width: 108px; background: var(--gold); color: var(--white); line-height: 47px; }

  .hero-photo { position: absolute; top: 86px; left: 0; width: 1200px; height: 814px;
    background:
      radial-gradient(ellipse 300px 460px at 400px 560px, rgba(96, 68, 44, 0.55), transparent 72%),
      radial-gradient(ellipse 260px 300px at 560px 330px, rgba(214, 170, 130, 0.45), transparent 70%),
      radial-gradient(ellipse 420px 360px at 1150px 80px, rgba(216, 194, 180, 0.8), transparent 70%),
      linear-gradient(115deg, var(--field-light) 0%, var(--field-mid) 40%, #b8936a 70%, var(--field-haze) 100%); }
  .hero-photo::after { content: ""; position: absolute; inset: 0; background: linear-gradient(180deg, rgba(0,0,0,0.04), rgba(90,62,40,0.28)); }

  .hero-text { position: absolute; top: 150px; left: 0; right: 0; text-align: center; z-index: 2; text-shadow: 0 2px 6px rgba(0,0,0,0.35); }
  .hero-title { font-family: "Raleway", sans-serif; font-weight: 800; font-size: 84px; line-height: 1.1; letter-spacing: 1px; }
  .hero-tagline { margin-top: 12px; font-weight: 600; font-size: 31px; }
  .hero-quote { width: 790px; margin: 20px auto 0; font-style: italic; font-size: 22px; line-height: 37px; }

  .supporters { position: absolute; top: 0; left: 0; z-index: 1; }
  .supporters .ring { fill: var(--ring-fill); stroke: var(--ring); stroke-width: 5; }
  .supporters .avatar-shape { fill: var(--avatar); }

  .copyright { position: absolute; bottom: 46px; left: 0; right: 0; text-align: center; font-size: 16px; z-index: 2; }
</style>
</head>
<body>
<main class="screen">
  <header class="topbar">
    <div class="menu-toggle" aria-label="Menu"><span></span><span></span><span></span></div>
    <a class="nav-link" href="#mission">SEE THE MISSION</a>
    <svg class="search-icon" width="24" height="24" viewBox="0 0 24 24" aria-label="Search">
      <circle cx="9.5" cy="9.5" r="7" fill="none" stroke="#ffffff" stroke-width="3"/>
      <line x1="14.5" y1="14.5" x2="21.5" y2="21.5" stroke="#ffffff" stroke-width="3.5" stroke-linecap="round"/>
    </svg>
    <div class="brand">HALO FUNDRY</div>
    <a class="btn btn-login" href="#login">LOGIN</a>
    <a class="btn btn-signup" href="#signup">SIGN UP</a>
  </header>

  <div class="hero-photo" role="img" aria-label="Photo of a young girl in a checked summer dress kneeling in a golden wheat field, hands together in prayer, looking upward"></div>

  <svg class="supporters" width="1200" height="900" viewBox="0 0 1200 900" aria-label="Supporter avatars">
    <defs>
      <clipPath id="avatar-clip"><circle cx="0" cy="0" r="0.9"/></clipPath>
      <symbol id="avatar" viewBox="-1 -1 2 2" overflow="visible">
        <circle class="ring" cx="0" cy="0" r="0.95" vector-effect="non-scaling-stroke"/>
        <g clip-path="url(#avatar-clip)">
          <circle class="avatar-shape" cx="0" cy="-0.2" r="0.32"/>
          <path class="avatar-shape" d="M-0.72 0.95 C-0.72 0.45 -0.4 0.2 0 0.2 C0.4 0.2 0.72 0.45 0.72 0.95 Z"/>
        </g>
      </symbol>
    </defs>
    <use href="#avatar" x="1026" y="252" width="132" height="132"/>
    <use href="#avatar" x="654" y="415" width="124" height="124"/>
    <use href="#avatar" x="887" y="381" width="130" height="130"/>
    <use href="#avatar" x="1028" y="446" width="98" height="98"/>
    <use href="#avatar" x="804" y="496" width="96" height="96"/>
    <use href="#avatar" x="901" y="590" width="124" height="124"/>
    <use href="#avatar" x="1065" y="631" width="86" height="86"/>
    <use href="#avatar" x="734" y="652" width="128" height="128"/>
    <use href="#avatar" x="918" y="738" width="128" height="128"/>
  </svg>

  <section class="hero-text">
    <h1 class="hero-title">HALO FUNDRY</h1>
    <p class="hero-tagline">We are christian crowd funding</p>
    <p class="hero-quote">“ she has a name. He has dreams. She hope she could have a future. He is like you.” 1 USD a month will help her and him.”</p>
  </section>

  <footer class="copyright">Copyrights © 2016, Halo Fundry. All rights reserved.</footer>
</main>
</body>
</html>
```